Bright Farm Stationery & Business Card
Stationery Designs for Agricultural Consulting company
Creative Brief
Bright & Fun-filled
Dennis & Marla Pickstone
427 Quillmoor Bend Lane Seffner, FL 33584
Dennis 813-555-0147
Marla 813-555-0183
brightfarmhelp@plowmail.example
Final design will need to have cards for 2 other salesmen info - name, cell & email would be different than above

```html
<!DOCTYPE html>
<html lang="en">
<head>
<meta charset="utf-8">
<title>Bright Farm Stationery &amp; Business Card</title>
<link href="https://fonts.googleapis.com/css2?family=Open+Sans:wght@400;700&display=swap" rel="stylesheet">
<style>
  :root {
    --stage: #d9dadc;
    --paper: #ffffff;
    --logo-ink: #cfe6ff;
    --sun: #f2d25a;
    --ink-light: #e6eef7;
    --teal-light: #5fe0c4;
    --paper-edge: #c9cbce;
  }
  * { margin: 0; padding: 0; box-sizing: border-box; }
  html, body { width: 1200px; height: 1040px; overflow: hidden; }
  body {
    background: var(--stage);
    font-family: "Open Sans", Arial, sans-serif;
    position: relative;
  }
  .piece { position: absolute; background: var(--paper); border: 1px solid var(--paper-edge); overflow: hidden; }
  .piece svg.band { position: absolute; left: 0; top: 0; }
  .letterhead { left: 421px; top: 51px; width: 647px; height: 927px; }
  .envelope { left: 205px; top: 470px; width: 672px; height: 373px; }
  .business-card { left: 851px; top: 236px; width: 318px; height: 174px; border: none; }

  .brand {
    position: absolute;
    display: flex; align-items: center; gap: 6px;
    font-weight: 700;
    color: var(--logo-ink);
    white-space: nowrap;
    line-height: 1;
  }
  .brand .mark { border-radius: 50%; background: var(--sun); flex: none; }

  .contact { position: absolute; color: var(--ink-light); line-height: 1.6; white-space: nowrap; }

  .letterhead .brand { left: 22px; top: 52px; font-size: 30px; }
  .letterhead .brand .mark { width: 22px; height: 22px; }
  .letterhead .contact { left: 24px; top: 98px; font-size: 8px; }

  .envelope .brand { left: 22px; top: 48px; font-size: 30px; }
  .envelope .brand .mark { width: 22px; height: 22px; }
  .envelope .contact { left: 24px; top: 104px; font-size: 11px; }

  .business-card .brand { left: 14px; top: 28px; font-size: 24px; }
  .business-card .brand .mark { width: 18px; height: 18px; }
  .business-card .card-names { position: absolute; left: 18px; top: 80px; font-size: 8.5px; color: var(--teal-light); white-space: nowrap; }
  .business-card .card-address { left: 18px; top: 102px; font-size: 7px; }
  .business-card .card-phones { left: 186px; top: 80px; font-size: 7px; }
  .business-card .card-email { position: absolute; left: 186px; top: 112px; font-size: 6.5px; color: var(--ink-light); white-space: nowrap; }
</style>
</head>
<body>

<section class="piece letterhead" aria-label="Letterhead">
  <svg class="band" width="647" height="927" viewBox="0 0 647 927" aria-hidden="true">
    <defs>
      <linearGradient id="lh-navy" x1="0" y1="0" x2="1" y2="1">
        <stop offset="0" stop-color="#061024"/>
        <stop offset="0.55" stop-color="#13305a"/>
        <stop offset="1" stop-color="#0d4a6a"/>
      </linearGradient>
      <linearGradient id="lh-glow" x1="0" y1="1" x2="1" y2="0">
        <stop offset="0" stop-color="#0b3a6b"/>
        <stop offset="0.5" stop-color="#1fb39a"/>
        <stop offset="1" stop-color="#5fe0c4"/>
      </linearGradient>
    </defs>
    <path d="M0 0 H647 V20 C450 70 200 200 0 430 Z" fill="url(#lh-glow)"/>
    <path d="M0 0 H647 C440 40 190 180 0 395 Z" fill="url(#lh-navy)"/>
  </svg>
  <div class="brand"><span class="mark"></span>Bright Farm</div>
  <div class="contact">
    427 Quillmoor Bend Lane<br>
    Larkvale, FL 34990<br>
    Dennis: 813-555-0147<br>
    Marla: 813-555-0183<br>
    brightfarmhelp@plowmail.example
  </div>
</section>

<section class="piece envelope" aria-label="Envelope">
  <svg class="band" width="672" height="373" viewBox="0 0 672 373" aria-hidden="true">
    <defs>
      <linearGradient id="env-navy" x1="0" y1="0" x2="1" y2="1">
        <stop offset="0" stop-color="#061024"/>
        <stop offset="0.6" stop-color="#13305a"/>
        <stop offset="1" stop-color="#0d4a6a"/>
      </linearGradient>
      <linearGradient id="env-glow" x1="0" y1="1" x2="1" y2="0">
        <stop offset="0" stop-color="#0b3a6b"/>
        <stop offset="0.5" stop-color="#1fb39a"/>
        <stop offset="1" stop-color="#5fe0c4"/>
      </linearGradient>
    </defs>
    <path d="M0 0 H672 V14 C420 50 110 180 0 373 Z" fill="url(#env-glow)"/>
    <path d="M0 0 H672 C400 30 90 160 0 340 Z" fill="url(#env-navy)"/>
  </svg>
  <div class="brand"><span class="mark"></span>Bright Farm</div>
  <div class="contact">
    427 Quillmoor Bend Lane<br>
    Larkvale, FL 34990
  </div>
</section>

<section class="piece business-card" aria-label="Business card">
  <svg class="band" width="318" height="174" viewBox="0 0 318 174" aria-hidden="true">
    <defs>
      <linearGradient id="bc-navy" x1="0" y1="0" x2="1" y2="1">
        <stop offset="0" stop-color="#061024"/>
        <stop offset="0.6" stop-color="#13305a"/>
        <stop offset="1" stop-color="#0a2346"/>
      </linearGradient>
      <radialGradient id="bc-glow" cx="0.85" cy="0.1" r="0.6">
        <stop offset="0" stop-color="#5fe0c4" stop-opacity="0.85"/>
        <stop offset="0.5" stop-color="#1fb39a" stop-opacity="0.35"/>
        <stop offset="1" stop-color="#1fb39a" stop-opacity="0"/>
      </radialGradient>
    </defs>
    <rect width="318" height="174" fill="url(#bc-navy)"/>
    <rect width="318" height="174" fill="url(#bc-glow)"/>
  </svg>
  <div class="brand"><span class="mark"></span>Bright Farm</div>
  <div class="card-names">Dennis &amp; Marla Pickstone</div>
  <div class="contact card-address">
    427 Quillmoor Bend Lane<br>
    Larkvale, FL 34990
  </div>
  <div class="contact card-phones">
    Dennis: 813-555-0147<br>
    Marla: 813-555-0183
  </div>
  <div class="card-email">brightfarmhelp@plowmail.example</div>
</section>

</body>
</html>
```